New Website for Corriveld House at www.corriveld.com.au

A new logo has been designed (through pixel forum) and we now want to align the look and feel of our website at www.corriveld.com.au to the new logo. The content and page names (e.g. Grounds) will remain largely unchanged for the new site, so please submit a new look "Home" page, using our new logo, current text and any photos you choose from the existing gallery at our website. I have also attached the current "Home" page photos.

Industry/Entity Type

Accommodation

Number of Pages Required

1 page

Requirements
Must have
• Logo to be presented on white background.

```html
<!DOCTYPE html>
<html lang="en">
<head>
<meta charset="utf-8">
<title>Corriveld House – Options to Sleep More</title>
<link href="https://fonts.googleapis.com/css2?family=Montserrat:wght@300;400&display=swap" rel="stylesheet">
<style>
  :root {
    --ink: #1c1c1c;
    --rule: #bdbdbd;
    --sun: #f6cf2e;
    --white: #ffffff;
    --night: #1b2024;
    --tile-blue: rgba(22, 86, 150, 0.88);
    --warm-1: #e9c9a3;
    --warm-2: #c98e5c;
    --room-1: #efe5da;
    --room-2: #a68a7a;
  }
  * { margin: 0; padding: 0; box-sizing: border-box; }
  html, body { width: 1200px; height: 1200px; overflow: hidden; background: var(--white); }
  body { font-family: "Montserrat", sans-serif; color: var(--ink); position: relative; }

  .section-title {
    position: absolute; left: 0; width: 1200px; text-align: center;
    font-weight: 300; font-size: 37px; letter-spacing: 1.5px;
  }
  .divider { position: absolute; height: 1px; background: var(--rule); }
  .divider-mark {
    position: absolute; width: 11px; height: 11px; background: var(--sun);
    transform: rotate(45deg);
  }

  .intro {
    position: absolute; left: 0; top: 84px; width: 1200px; text-align: center;
    font-size: 12.6px; line-height: 21.6px; font-weight: 400; white-space: nowrap;
    letter-spacing: -0.1px;
  }

  .feature { position: absolute; left: 88px; width: 1024px; height: 339px; overflow: hidden; }
  .feature-photo { position: absolute; top: 0; height: 100%; }
  .apartment { top: 152px; }
  .apartment .feature-photo {
    left: 452px; width: 572px;
    background: linear-gradient(90deg, var(--white) 0%, rgba(255,255,255,0) 22%),
                linear-gradient(180deg, #ece9e4 0%, #d9c7b2 45%, var(--warm-1) 70%, var(--warm-2) 100%);
  }
  .sports { top: 491px; }
  .sports .feature-photo {
    left: 0; width: 600px;
    background: linear-gradient(270deg, var(--white) 0%, rgba(255,255,255,0) 25%),
                linear-gradient(180deg, var(--room-1) 0%, #d8c6b4 50%, var(--room-2) 100%);
  }
  .feature-heading {
    position: absolute; font-weight: 300; font-size: 30px; letter-spacing: 1px;
    padding-bottom: 6px; border-bottom: 1px solid var(--ink); white-space: nowrap;
  }
  .feature-text {
    position: absolute; font-size: 12.6px; line-height: 21.6px; white-space: nowrap;
    letter-spacing: -0.1px;
  }
  .feature-text p + p { margin-top: 21.6px; }

  .gallery {
    position: absolute; left: 88px; top: 830px; width: 1024px; height: 370px; overflow: hidden;
    background: linear-gradient(180deg, #252b27 0%, #2b2a26 35%, var(--night) 100%);
  }
  .gallery .section-title { color: var(--white); left: 0; width: 1024px; top: 63px; }
  .gallery .divider { background: #6d6f70; }
  .tile { position: absolute; width: 233px; height: 206px; }
  .tile-cover { background: linear-gradient(180deg, #3b5f7d, #24435f); }
  .tile-overlay {
    position: absolute; inset: 0; background: var(--tile-blue);
    display: flex; flex-direction: column; align-items: center; justify-content: center;
    color: var(--white); font-size: 17px; line-height: 24px; text-align: center;
  }
  .tile-overlay svg { margin: 20px 0 12px; }
  .tile-lounge { background: linear-gradient(180deg, #ece6dc 0%, #d6c8b2 55%, #6b5642 100%); }
  .tile-stairs { background: linear-gradient(180deg, #f1ece3 0%, #d4b79a 60%, #9b6d4a 100%); }
  .tile-doors  { background: linear-gradient(180deg, #e7d2a8 0%, #e1c7a0 55%, #b07a52 100%); }
  .tile-next   { background: linear-gradient(180deg, #6a7076, #3f4449); }
</style>
</head>
<body>

  <h1 class="section-title" style="top:16px;">OPTIONS TO SLEEP MORE!</h1>
  <div class="divider" style="left:349px; top:68px; width:503px;"></div>
  <div class="divider-mark" style="left:594px; top:63px;"></div>

  <p class="intro">The owner’s private apartment and guest room are now available to the public. If you want more space or need to sleep up to 26 people<br>– Corriveld House can accommodate you.</p>

  <section class="feature apartment">
    <div class="feature-photo" role="img" aria-label="Open plan apartment with leather lounges, coffee table, tiled floor and kitchen"></div>
    <h2 class="feature-heading" style="left:44px; top:42px;">OWNER’S APARTMENT</h2>
    <div class="feature-text" style="left:46px; top:100px;">
      <p>The open plan apartment contains a living room, dining area and<br>kitchen – plus a large bedroom with king size bed, ensuite and<br>walk-in robe.</p>
      <p>For special guests, the apartment is a fabulous haven in the heart<br>of the estate!</p>
      <p>Although large in size, we do not permit more than 2 guests to<br>stay in the apartment – prices upon application.</p>
    </div>
  </section>

  <section class="feature sports">
    <div class="feature-photo" role="img" aria-label="Guest bedroom with double bed, bedside lamps and framed sporting memorabilia"></div>
    <h2 class="feature-heading" style="left:603px; top:50px;">SPORTS ROOM</h2>
    <div class="feature-text" style="left:603px; top:109px;">
      <p>Located in the Wren &amp; Willow building, the bedroom sleeps 2<br>(double bed) and is adorned with sporting memorabilia.</p>
      <p>A full bathroom in the Wren &amp; Willow provides the amenities –<br>prices upon application.</p>
    </div>
  </section>

  <section class="gallery" role="img" aria-label="Dusk view of the estate grounds and rooftops behind the gallery">
    <h2 class="section-title">PHOTO GALLERY</h2>
    <div class="divider" style="left:342px; top:120px; width:342px;"></div>
    <div class="divider-mark" style="left:507px; top:115px;"></div>

    <div class="tile tile-cover" style="left:45px; top:147px;" role="img" aria-label="Mansion exterior at dusk">
      <div class="tile-overlay">
        <svg width="48" height="48" viewBox="0 0 48 48" fill="none" stroke="#fff" stroke-width="4" stroke-linecap="round">
          <circle cx="20" cy="20" r="15"/>
          <line x1="31" y1="31" x2="44" y2="44"/>
          <line x1="20" y1="12" x2="20" y2="28"/>
          <line x1="12" y1="20" x2="28" y2="20"/>
        </svg>
        <span>Click here to<br>view image</span>
      </div>
    </div>
    <div class="tile tile-lounge" style="left:279px; top:147px;" role="img" aria-label="Double height lounge with black leather sofas and fireplace"></div>
    <div class="tile tile-stairs" style="left:513px; top:147px;" role="img" aria-label="Curved staircase in the entrance hall"></div>
    <div class="tile tile-doors" style="left:748px; top:147px;" role="img" aria-label="Staircase seen through open French doors"></div>

    <div class="tile tile-next" style="left:45px; top:356px;"></div>
    <div class="tile tile-next" style="left:279px; top:356px;"></div>
    <div class="tile tile-next" style="left:513px; top:356px;"></div>
    <div class="tile tile-next" style="left:748px; top:356px;"></div>
  </section>

</body>
</html>
```